Can you create a Business Card based on the Logo you designed.

See example and would like to see other examples.

Trying to keep it very clean with a focus on the logo and name.

```html
<!DOCTYPE html>
<html lang="en">
<head>
<meta charset="utf-8">
<title>Fieldmark Business Card</title>
<link rel="stylesheet" href="https://fonts.googleapis.com/css2?family=Montserrat:wght@600;700;800&family=Open+Sans:wght@400&display=swap">
<style>
  :root {
    --backdrop: #2b2b2b;
    --brand-green: #0e7344;
    --leaf-green: #7dc242;
    --sun-orange: #f39a2c;
    --paper: #ffffff;
    --ink: #333333;
  }
  * { margin: 0; padding: 0; box-sizing: border-box; }
  html, body {
    width: 1200px; height: 689px; overflow: hidden;
    background: var(--backdrop);
  }
  .canvas {
    width: 1200px; height: 689px;
    display: flex; align-items: center; justify-content: center; gap: 60px;
  }
  .card {
    position: relative;
    width: 510px; height: 292px;
    border-radius: 22px;
    overflow: hidden;
  }
  .card--front {
    background: var(--brand-green);
    display: flex; align-items: center; justify-content: center;
  }
  .wordmark {
    display: flex; align-items: center; gap: 12px;
    font-family: "Montserrat", sans-serif;
    font-weight: 700;
    letter-spacing: 0.5px;
  }
  .wordmark__dot {
    border-radius: 50%;
    background: var(--sun-orange);
  }
  .card--front .wordmark { font-size: 58px; color: var(--paper); }
  .card--front .wordmark__dot { width: 30px; height: 30px; }

  .card--back { background: var(--paper); }
  .card--back .wordmark {
    position: absolute; top: 58px; right: 40px;
    font-size: 36px; color: var(--brand-green);
  }
  .card--back .wordmark__dot { width: 20px; height: 20px; }
  .divider {
    position: absolute; left: 46px; right: 40px; top: 186px;
    height: 1px; background: var(--sun-orange);
  }
  .person {
    position: absolute; left: 46px; top: 126px;
  }
  .person__name {
    font-family: "Montserrat", sans-serif;
    font-weight: 800; font-size: 27px;
    color: var(--brand-green);
    text-transform: uppercase; line-height: 1;
    letter-spacing: -0.3px;
  }
  .person__title {
    font-family: "Open Sans", sans-serif;
    font-size: 15px; color: var(--leaf-green);
    margin-top: 6px;
  }
  .contacts {
    position: absolute; left: 46px; top: 198px;
    list-style: none;
    font-family: "Open Sans", sans-serif;
    font-size: 13.5px; color: var(--ink);
  }
  .contacts li {
    display: flex; align-items: center; gap: 9px;
    height: 22px;
  }
  .contacts svg { width: 13px; height: 13px; flex: none; }
</style>
</head>
<body>
<main class="canvas">
  <section class="card card--front" aria-label="Card front">
    <div class="wordmark"><span class="wordmark__dot"></span>Fieldmark</div>
  </section>

  <section class="card card--back" aria-label="Card back">
    <div class="wordmark"><span class="wordmark__dot"></span>Fieldmark</div>
    <div class="person">
      <h1 class="person__name">Marcus Hale</h1>
      <p class="person__title">Chief Executive Officer</p>
    </div>
    <div class="divider"></div>
    <ul class="contacts">
      <li>
        <svg viewBox="0 0 14 14" aria-hidden="true"><rect x="3.5" y="1" width="7" height="12" rx="1.5" fill="none" stroke="#7dc242" stroke-width="1.4"/><circle cx="7" cy="10.7" r="0.8" fill="#7dc242"/></svg>
        +1 (555) 014-2290
      </li>
      <li>
        <svg viewBox="0 0 14 14" aria-hidden="true"><rect x="1" y="3" width="12" height="8" fill="#7dc242"/><path d="M1 3 L7 8 L13 3" fill="none" stroke="#fff" stroke-width="1.2"/></svg>
        ceo@fieldmark.com
      </li>
      <li>
        <svg viewBox="0 0 14 14" aria-hidden="true"><circle cx="7" cy="7" r="6" fill="#7dc242"/><ellipse cx="7" cy="7" rx="2.6" ry="6" fill="none" stroke="#fff" stroke-width="1"/><line x1="1" y1="7" x2="13" y2="7" stroke="#fff" stroke-width="1"/></svg>
        www.fieldmark.com
      </li>
    </ul>
  </section>
</main>
</body>
</html>
```